Web Page needed for Dr. Wanbrook Consult

The company works in the consultant business for processes in large projects our of engineering and construction business. We develop strategies but work also in critical projects to get them right.
The page should have a modern appearance but though a classy and luxury touch.
Updates

The project was bought in a package, logo plus web page. Now the designers do submit logos again, although the logo has been set. This part is only the web site. I changed the text to clarify it, I contacted support to put that right, but that needs an extension of minimum 7 days to catch up.

Due to the confusion in the project, it was first set up as logo project and later corrected (I have no clue how that happened, as I bought a package with logo + web, and logo is already done), there is a large delay in getting feedback. Please be so kind and extend until 31.01. In Europe there is holidays until 07.01. and I have no time to discuss the topics with my client until 10.01., than we need to feed in response and get changes done.

Logo Text

The logo is already fixed, I asked for web page.

Number of Pages Required

5+ page

Font styles to use
Sans Serif

Colors

Designer to choose colors to be used in the design.

Requirements
Must have
• Home/Start
• Lean Construction
• Lean Equipment
• Lean Design
• Lean Training
• Team
• Contact
• Imprint
Nice to have
• Darker color, luxury appearance, please integrate the logo in the attachment here.
• I would like to have a web page with animated context, such as this one here: https://tovalmerworks.example

```html
<!DOCTYPE html>
<html lang="en">
<head>
<meta charset="utf-8">
<title>Dr. Wanbrook Consult</title>
<link href="https://fonts.googleapis.com/css2?family=Poppins:ital,wght@0,400;0,500;0,600;0,700;1,400&display=swap" rel="stylesheet">
<style>
:root{
  --dark:#2f343b;
  --dark-2:#2a2d32;
  --tile-a:#2b2e33;
  --tile-b:#35383d;
  --green:#8dc63f;
  --blue:#2f7fc1;
  --ink:#1f2328;
  --muted:#5d636b;
  --light:#f2f5f8;
  --white:#ffffff;
}
*{margin:0;padding:0;box-sizing:border-box}
html,body{width:1200px;height:5075px;overflow:hidden}
body{position:relative;background:var(--white);font-family:"Poppins",sans-serif;color:var(--ink)}
.abs{position:absolute}
.fill{position:absolute}
.label{position:absolute;font-size:13px;font-weight:600;color:var(--green);text-transform:uppercase;letter-spacing:.3px;display:flex;align-items:center;gap:8px}
.label::before{content:"";width:26px;height:2px;background:var(--green)}
.label.blue{color:var(--blue)}
.label.blue::before{background:var(--green)}
.title{position:absolute;font-weight:700;text-transform:uppercase;line-height:1.1;letter-spacing:-.3px;white-space:nowrap}
.text{position:absolute;font-size:12.5px;line-height:22px;color:var(--muted)}
.btn{position:absolute;background:var(--green);color:#fff;font-size:11px;font-weight:600;text-transform:uppercase;display:flex;align-items:center;justify-content:center}

/* header */
.logo{position:absolute;display:flex;align-items:center;gap:8px;color:var(--blue);font-weight:500;font-size:19px;letter-spacing:.5px;text-transform:uppercase}
.logo-square{width:30px;height:30px;background:var(--blue)}
.nav{position:absolute;left:666px;top:38px;display:flex;gap:0;font-size:13px;font-weight:500;color:var(--ink)}
.nav a{position:absolute;white-space:nowrap;color:inherit;text-decoration:none}
.nav a.active::after{content:"";position:absolute;left:0;right:0;bottom:-10px;height:2px;background:var(--green)}

.hero-bg{left:0;top:0;width:1200px;height:630px;background:linear-gradient(180deg,#eef2f6 0%,#f7f9fb 70%,#ffffff 100%)}
.hero-title{left:93px;color:var(--ink)}
.slider{position:absolute;left:93px;top:516px;display:flex;gap:0;font-size:12px;color:#9aa0a6}
.slider span{width:84px;padding-bottom:8px;border-bottom:2px solid #dde1e5}
.slider span.on{color:var(--green);border-bottom-color:var(--green)}

/* services */
.card-cap{position:absolute;background:#fff;border:2px solid #dcdfe3;border-top:none;text-align:center}
.card-cap h3{font-size:18px;font-weight:600;margin-top:20px}
.card-cap p{font-size:11px;color:var(--green);margin-top:4px}
.card-cap.on{border-color:var(--green);border-left-color:var(--blue)}

/* clients */
.tile{position:absolute;width:203px;height:202px;display:flex;align-items:center;justify-content:center}
.tile.a{background:var(--tile-a)}
.tile.b{background:var(--tile-b)}
.tile span{width:64px;height:64px;border-radius:50%;background:#5c6066}

/* testimonials */
.avatar{position:absolute;transform:rotate(45deg);border-radius:16px}

/* footer */
.footer{left:0;top:4704px;width:1200px;height:371px;background:var(--dark)}
.foot-h{position:absolute;top:4788px;color:#fff;font-size:14px;font-weight:600}
.foot-h::after{content:"";display:block;width:42px;height:2px;background:var(--green);margin-top:8px}
.foot-list{position:absolute;top:4834px;list-style:none;font-size:11.5px;color:#aeb3b9;line-height:27px}
.contact-row{display:flex;gap:10px;align-items:flex-start}
</style>
</head>
<body>

<!-- HERO -->
<div class="fill hero-bg" role="img" aria-label="Faded glass office towers in the background"></div>
<div class="logo" style="left:93px;top:30px"><span class="logo-square"></span>Dr. Wanbrook Consult</div>
<nav class="nav">
  <a class="active" style="left:0">Home</a>
  <a style="left:83px">About us</a>
  <a style="left:185px">Services</a>
  <a style="left:284px">Projects</a>
  <a style="left:380px">Contacts</a>
</nav>
<div class="fill" role="img" aria-label="Business consultants meeting at a desk with a laptop, tinted blue" style="left:591px;top:98px;width:516px;height:444px;background:linear-gradient(135deg,#2b6fb3 0%,#4c92d0 55%,#9cc3e6 100%)"></div>
<div class="label" style="left:93px;top:211px">Consultant business for</div>
<div class="title hero-title" style="top:236px;font-size:35px;font-weight:600">Large projects our of</div>
<div class="title hero-title" style="top:284px;font-size:50px">Engineering and</div>
<div class="title hero-title" style="top:346px;font-size:35px">Construction business</div>
<div class="btn" style="left:93px;top:418px;width:137px;height:37px">Know more</div>
<div class="slider"><span class="on">01</span><span>02</span><span>03</span></div>

<!-- ABOUT -->
<div class="fill" role="img" aria-label="City skyline in a green to blue gradient" style="left:0;top:693px;width:392px;height:540px;background:linear-gradient(180deg,#8dc63f 0%,#4fa37a 45%,#2f7fc1 100%)"></div>
<div class="fill" style="left:272px;top:644px;width:928px;height:540px;background:var(--dark)"></div>
<div class="label blue" style="left:337px;top:768px">About us</div>
<div class="title" style="left:337px;top:796px;font-size:33px;letter-spacing:-.6px;color:#fff">Dr. Wanbrook Consult</div>
<div class="text" style="left:337px;top:861px;width:460px;color:#c7ccd2;font-size:12px">Vivamus faucibus erat ut enim tincidunt, vitae ullamcorper erat tristique. Ut nec imperdiet sapien, maximus dictum nisi. Sed tempus neque vel neque commodo, eget euismod eros cursus. Nunc at ura ut arcu blandit malesuada id vl sem. Proin pulinar a ipsum non sucipit. Sed quis euismod elit. Maecenas elementum eu odio vitae consectetur. Duis quis commodo augue. Nunc ornare ante ac leo pellentesque, quis cursus risus fringilla.</div>
<div class="btn" style="left:337px;top:1020px;width:137px;height:38px">Know more</div>
<div class="fill" role="img" aria-label="Two businessmen in suits reviewing documents at a table" style="left:829px;top:747px;width:278px;height:358px;background:linear-gradient(160deg,#e9ecef 0%,#b7c0ca 50%,#2e3a4a 100%);border:1px solid #fff"></div>

<!-- SERVICES -->
<div class="label blue" style="left:93px;top:1304px">Services</div>
<div class="title" style="left:93px;top:1328px;font-size:40px">Our services</div>
<div class="text" style="left:93px;top:1382px;width:550px;font-size:12px">Vivamus faucibus erat ut enim tincidunt, vitae ullamcorper erat tristique. Ut nec imperdiet sapien, maximus dictum nisi. Sed tempus neque vel neque commodo, eget euismod eros cursus. Nunc at ura ut arcu</div>
<div class="btn" style="left:953px;top:1395px;width:154px;height:39px">View all services</div>

<div class="fill" role="img" aria-label="Engineers in hard hats reviewing plans" style="left:93px;top:1481px;width:323px;height:249px;background:linear-gradient(160deg,#f1efe9 0%,#c9c2b5 50%,#4a4e55 100%)"></div>
<div class="card-cap" style="left:110px;top:1730px;width:290px;height:98px"><h3>Vivamus Faucibus</h3><p>Know More</p></div>
<div class="fill" role="img" aria-label="Construction cranes over a building site at sunset" style="left:437px;top:1481px;width:323px;height:249px;background:linear-gradient(180deg,#1f4f86 0%,#4a7fb0 45%,#e5b247 80%,#3b3325 100%)"></div>
<div class="card-cap on" style="left:455px;top:1730px;width:290px;height:98px"><h3>Vivamus Faucibus</h3><p>Know More</p></div>
<svg class="abs" style="left:593px;top:1818px" width="14" height="9" viewBox="0 0 14 9"><path d="M0 9 L7 0 L14 9 Z" fill="#2f7fc1"/></svg>
<div class="fill" role="img" aria-label="Business handshake over a desk" style="left:782px;top:1481px;width:323px;height:249px;background:linear-gradient(150deg,#55585c 0%,#9a9b9c 50%,#e3e3e1 100%)"></div>
<div class="card-cap" style="left:800px;top:1730px;width:290px;height:98px"><h3>Vivamus Faucibus</h3><p>Know More</p></div>

<!-- EXPERIENCE -->
<div class="fill" role="img" aria-label="Consultants at work in a green to blue tinted office" style="left:806px;top:1946px;width:394px;height:540px;background:linear-gradient(180deg,#8dc63f 0%,#4fa37a 45%,#2f7fc1 100%)"></div>
<div class="fill" style="left:0;top:1897px;width:924px;height:540px;background:var(--dark)"></div>
<div class="label blue" style="left:93px;top:1992px">Consultant business</div>
<div class="title" style="left:93px;top:2014px;font-size:40px;color:#fff;line-height:48px">We have expereince<br>in consulting</div>
<div class="text" style="left:93px;top:2132px;width:780px;color:#c7ccd2;font-size:12px">Vivamus faucibus erat ut enim tincidunt, vitae ullamcorper erat tristique. Ut nec imperdiet sapien, maximus dictum nisi. Sed tempus neque vel neque commodo, eget euismod eros cursus. Nunc at ura ut arcu blandit malesuada id vl sem. Proin pulinar a ipsum non sucipit. Sed quis euismod elit. Maecenas elementum eu odio vitae consectetur. Duis quis commodo augue. Nunc ornare ante ac leo pellentesque, quis cursus risus fringilla. Vivamus faucibus erat ut enim tincidunt, vitae ullamcorper erat tristique. Ut nec imperdiet sapien, maximus dictum nisi. Sed tempus neque vel neque commodo, eget euismod eros cursus. Nunc at urna ut arcu blandit malesuada id vl sem. Proin pulinar a ipsum non suscipit. Sed quis euismod elit. Maecenas elementum eu odio vitae consectetur. Duis quis commodo augue. Nunc ornare ante ac leo pellentesque, quis cursus risus fringilla.</div>

<!-- PROJECTS -->
<div class="label blue" style="left:93px;top:2543px">Projects</div>
<div class="title" style="left:93px;top:2567px;font-size:40px">Recent projects</div>
<div class="fill" role="img" aria-label="Building under construction wrapped in scaffolding" style="left:93px;top:2626px;width:500px;height:284px;background:linear-gradient(180deg,#6fa3d8 0%,#a9c8e4 40%,#a08a5a 75%,#5a4a30 100%)"></div>
<div class="fill" role="img" aria-label="Glass skyscrapers seen from below against a blue sky" style="left:93px;top:2925px;width:500px;height:343px;background:linear-gradient(160deg,#2a6bb5 0%,#6ea6da 50%,#cfe1f1 100%)"></div>
<div class="fill" role="img" aria-label="Looking up at glass towers with the sun between them" style="left:607px;top:2543px;width:498px;height:284px;background:linear-gradient(150deg,#3b6fa7 0%,#f7f1de 50%,#4a78ac 100%)"></div>
<div class="fill" role="img" aria-label="Pale glass office towers rising into a bright sky" style="left:607px;top:2845px;width:498px;height:423px;background:linear-gradient(160deg,#e6ebef 0%,#b7c3cf 55%,#6d7c8c 100%)"></div>
<div class="btn" style="left:532px;top:3292px;width:136px;height:37px">Know more</div>

<!-- CLIENTS -->
<div class="fill" style="left:0;top:3408px;width:1200px;height:404px;background:var(--dark)"></div>
<div class="label blue" style="left:533px;top:3459px">Partenaires</div>
<div class="title" style="left:0;width:1200px;text-align:center;top:3485px;font-size:40px;color:#fff">Clients &amp; Partenaires</div>

<div class="tile a" style="left:93px;top:3585px"><span></span></div>
<div class="tile a" style="left:93px;top:3787px"><span></span></div>
<div class="tile b" style="left:296px;top:3640px"><span></span></div>
<div class="tile a" style="left:296px;top:3842px"><span></span></div>
<div class="tile a" style="left:499px;top:3585px"><span></span></div>
<div class="tile b" style="left:499px;top:3787px"><span></span></div>
<div class="tile b" style="left:702px;top:3640px"><span></span></div>
<div class="tile a" style="left:702px;top:3842px"><span></span></div>
<div class="tile b" style="left:904px;top:3585px"><span></span></div>
<div class="tile a" style="left:904px;top:3787px"><span></span></div>

<!-- TESTIMONIALS -->
<div class="label blue" style="left:527px;top:4121px">Testimonials</div>
<div class="title" style="left:0;width:1200px;text-align:center;top:4146px;font-size:40px">Customer are saying</div>
<div class="avatar" role="img" aria-label="Customer portrait" style="left:417px;top:4312px;width:64px;height:64px;background:linear-gradient(135deg,#eef1f4,#c7ced6)"></div>
<div class="avatar" role="img" aria-label="Featured customer portrait" style="left:546px;top:4256px;width:108px;height:108px;background:linear-gradient(135deg,#2f7fc1,#1b3f73);box-shadow:0 12px 24px rgba(0,0,0,.15)"></div>
<div class="avatar" role="img" aria-label="Customer portrait" style="left:719px;top:4312px;width:64px;height:64px;background:linear-gradient(135deg,#eef1f4,#c7ced6)"></div>
<svg class="abs" style="left:570px;top:4428px" width="70" height="44" viewBox="0 0 70 44"><path d="M4 44 Q0 18 18 6 L22 12 Q12 20 14 26 Q28 26 28 36 Q28 44 18 44 Z M40 44 Q36 18 54 6 L58 12 Q48 20 50 26 Q64 26 64 36 Q64 44 54 44 Z" fill="#8dc63f"/></svg>
<div class="text" style="left:260px;top:4489px;width:680px;text-align:center;font-style:italic;font-size:12px">Vivamus faucibus erat ut enim tincidunt, vitae ullamcorper erat tristique. Ut nec imperdiet sapien, maximus dictum nisi. Sed tempus neque vel neque commodo, eget euismod eros cursus. Nunc at ura ut arcu</div>
<div class="abs" style="left:0;width:1200px;text-align:center;top:4557px;font-size:15px;font-weight:500">Lorem ipsum</div>
<div class="abs" style="left:0;width:1200px;text-align:center;top:4580px;font-size:9px;color:#8a9097">Simply Dummy</div>
<svg class="abs" style="left:572px;top:4634px" width="56" height="10" viewBox="0 0 56 10"><circle cx="5" cy="5" r="4" fill="#2f7fc1"/><circle cx="28" cy="5" r="4" fill="#c9cdd2"/><circle cx="51" cy="5" r="4" fill="#c9cdd2"/></svg>

<!-- FOOTER -->
<footer class="fill footer"></footer>
<div class="logo" style="left:93px;top:4790px;font-size:17px"><span class="logo-square" style="width:26px;height:26px"></span>Dr. Wanbrook Consult</div>
<div class="text" style="left:93px;top:4838px;width:270px;color:#aeb3b9;font-size:11px;line-height:19px">Lorem ipsum dolor sit amet, conetur adipiscing elit. Aliquam vel risus et risus porttitor interdum ut sed elit. Sed ultrices ut purus sed tincidunt. Pellentesque vestibulum, arcu et gravida facilisis, lectus ex blandit lectus.</div>

<div class="foot-h" style="left:447px">Get In Touch</div>
<div class="foot-list" style="left:447px;width:300px">
  <div class="contact-row" style="color:#fff;font-weight:600;font-size:12.5px"><svg width="14" height="14" viewBox="0 0 14 14" style="margin-top:6px"><path d="M3 1 L5.5 1 L6.5 4 L5 5.2 Q6.3 8 8.8 9 L10 7.5 L13 8.5 L13 11 Q12.5 13 10.5 13 Q1 12 1 3.5 Q1 1 3 1 Z" fill="#8dc63f"/></svg>(001) 555-010-274</div>
  <div class="contact-row" style="line-height:18px;margin-top:6px"><svg width="14" height="16" viewBox="0 0 14 16" style="margin-top:2px"><path d="M7 0 Q13 0 13 6 Q13 10 7 16 Q1 10 1 6 Q1 0 7 0 Z" fill="#8dc63f"/><circle cx="7" cy="6" r="2.2" fill="#2f343b"/></svg><span>418 Larkspur Avenue<br>Suite 210<br>Merrow, GA 30000</span></div>
  <div class="contact-row" style="margin-top:8px"><svg width="14" height="11" viewBox="0 0 14 11" style="margin-top:8px"><rect width="14" height="11" rx="1" fill="#8dc63f"/><path d="M1 1.5 L7 6 L13 1.5" stroke="#2f343b" stroke-width="1.3" fill="none"/></svg>info@dr.wanbrookconsult.com</div>
</div>

<div class="foot-h" style="left:778px">Quick Links</div>
<ul class="foot-list" style="left:778px"><li>Home</li><li>About us</li><li>Services</li><li>Projects</li><li>Contacts</li></ul>

<div class="foot-h" style="left:983px">What we do</div>
<ul class="foot-list" style="left:983px"><li>Vivamus faucibus</li><li>Ullamcorper tristique</li><li>Integer augue</li><li>Fermentum vehicula</li><li>Metus vel</li></ul>

<div class="fill" style="left:0;top:5010px;width:1200px;height:1px;background:#444a52"></div>
<div class="abs" style="left:0;width:1200px;top:5033px;text-align:center;font-size:11px;color:#aeb3b9">© 2019 <span style="color:#8dc63f">Dr. Wanbrook Consult</span>. All Right Reserved.</div>

</body>
</html>
```